Vehicle graphics for healthcare company (bramblecovecare.co.uk)

I have a plain white van that needs some branding. I don't mind leaving a bit of the white, so I would consider a half wrap, or large panels of non-white, but I'm open to suggestion.

For a non-wrap design, I happened to see the KDT Van (attached photo), which I thought was a nice clear design. I thought maybe some elements of this could be included. Maybe their large A could be the S of my Bramble Cove logo.

The only two colours the company has used to date are the green and grey of the logo. 1B7F8C and 58585A.

The core business we provide is assessment for people about to purchase a wheelchair. We take their measurements, look at their clinical needs and then recommend a product for them to purchase.

The information we need on it:
- our logo (attached)
- Private Wheelchair Assessment
- Occupational Therapy
- Wheelchair Skills

Our contact details to be included:
- www.bramblecovecare.co.uk
- info@bramblecovecare.co.uk
- 02937 418205

Target Market(s)

Wheelchair users and other healthcare providers.

Industry/Entity Type

Healthcare

Font styles to use
Other font styles liked:
• Arthaus Medium

Requirements
Must have
• Logo, contact details. Green/grey colours. 1B7F8C and 58585A
Nice to have
• See attached van, I thought this was a simple, clear design.
Should not have
• Clutter.

```html
<!DOCTYPE html>
<html lang="en">
<head>
<meta charset="utf-8">
<title>Bramble Cove Therapy – Van Livery Options</title>
<link rel="stylesheet" href="https://fonts.googleapis.com/css2?family=Ubuntu:wght@400;500;700&display=swap">
<style>
  :root {
    --teal: #1B7F8C;
    --grey: #58585A;
    --body-white: #ffffff;
    --glass: #0c0c0c;
    --tyre: #151515;
    --backdrop: #ececec;
    --seam: #d4d4d4;
    --outline: #c9c9c9;
  }
  html, body {
    margin: 0;
    width: 1200px;
    height: 1200px;
    overflow: hidden;
    background: var(--backdrop);
    font-family: "Ubuntu", sans-serif;
  }
  .livery-sheet {
    width: 1200px;
    height: 1200px;
    display: flex;
    flex-direction: column;
    justify-content: space-between;
  }
  .livery-option {
    display: block;
    width: 1200px;
    height: 588px;
    background: linear-gradient(#f4f4f4, #e2e2e2);
  }
  .livery-option--grey { --panel: var(--grey); --rocker: var(--grey); --social: var(--teal); }
  .livery-option--teal { --panel: var(--teal); --rocker: var(--teal); --social: var(--grey); }

  .van-body { fill: var(--body-white); stroke: var(--outline); stroke-width: 1; }
  .van-glass { fill: var(--glass); }
  .van-seam { stroke: var(--seam); stroke-width: 1; fill: none; }
  .van-wheel { fill: var(--tyre); }
  .van-hub { fill: #3a3a3a; }
  .rear-panel { fill: var(--panel); }
  .rocker-stripe { fill: var(--rocker); }
  .frond-graphic { fill: var(--teal); }
  .social-strip { fill: var(--social); }
  .social-dot { fill: #ffffff; }

  .brand-name { fill: #ffffff; font-family: "Ubuntu", sans-serif; font-weight: 500; font-size: 19px; letter-spacing: 0.5px; }
  .brand-mark { fill: #ffffff; }
  .phone-number { fill: var(--teal); font-weight: 700; font-size: 20px; }
  .web-address { fill: var(--teal); font-weight: 700; font-size: 11.5px; }
  .email-address { fill: var(--teal); font-weight: 700; font-size: 10px; }
  .service-list { fill: var(--grey); font-weight: 700; font-size: 8px; }
  .service-bullet { fill: var(--teal); }
</style>
</head>
<body>
<main class="livery-sheet">

  <svg class="livery-option livery-option--grey" viewBox="0 0 960 470" role="group" aria-label="Livery option with grey rear panel">
    <path class="van-body" d="M70,300 L76,250 Q92,212 150,192 L232,128 Q252,110 302,108 L862,108 Q882,112 882,140 L882,340 Q878,360 860,362 L82,362 Q66,350 70,300 Z"/>
    <path class="van-glass" d="M188,216 L236,146 Q250,124 300,120 L388,118 L388,210 Z"/>
    <rect class="van-glass" x="418" y="115" width="194" height="90" rx="3"/>
    <path class="van-seam" d="M232,128 L232,355 M390,112 L390,355 M415,112 L415,355"/>
    <rect class="rocker-stripe" x="280" y="340" width="310" height="22"/>
    <path class="rear-panel" d="M680,108 L862,108 Q882,112 882,140 L882,340 Q878,360 860,362 L620,362 Q650,240 680,108 Z"/>
    <path class="frond-graphic" role="img" aria-label="Stylised fern frond and spine graphic sweeping down the side" d="M618,108 L680,108 Q650,240 620,362 L574,362 Q614,280 618,108 Z"/>

    <rect class="brand-mark" x="702" y="146" width="12" height="12"/>
    <text class="brand-name" x="720" y="158">BRAMBLE COVE</text>
    <text class="brand-name" x="864" y="182" text-anchor="end" style="font-size:13px">THERAPY</text>

    <rect class="social-strip" x="805" y="240" width="26" height="92"/>
    <circle class="social-dot" cx="818" cy="256" r="6"/>
    <circle class="social-dot" cx="818" cy="277" r="6"/>
    <circle class="social-dot" cx="818" cy="298" r="6"/>
    <circle class="social-dot" cx="818" cy="319" r="6"/>

    <text class="phone-number" x="243" y="262">02937 418205</text>
    <text class="web-address" x="243" y="281">www.bramblecovecare.co.uk</text>
    <text class="email-address" x="402" y="296" text-anchor="end">info@bramblecovecare.co.uk</text>
    <text class="service-list" x="420" y="270" textLength="176" lengthAdjust="spacingAndGlyphs"><tspan class="service-bullet">•</tspan> Occupational Therapy <tspan class="service-bullet">•</tspan> Wheelchair Skills</text>
    <text class="service-list" x="440" y="281" textLength="140" lengthAdjust="spacingAndGlyphs"><tspan class="service-bullet">•</tspan> Private Wheelchair Assessment</text>

    <circle class="van-wheel" cx="215" cy="362" r="52"/><circle class="van-hub" cx="215" cy="362" r="20"/>
    <circle class="van-wheel" cx="735" cy="362" r="52"/><circle class="van-hub" cx="735" cy="362" r="20"/>
  </svg>

  <svg class="livery-option livery-option--teal" viewBox="0 0 960 470" role="group" aria-label="Livery option with teal rear panel">
    <path class="van-body" d="M70,300 L76,250 Q92,212 150,192 L232,128 Q252,110 302,108 L862,108 Q882,112 882,140 L882,340 Q878,360 860,362 L82,362 Q66,350 70,300 Z"/>
    <path class="van-glass" d="M188,216 L236,146 Q250,124 300,120 L388,118 L388,210 Z"/>
    <rect class="van-glass" x="418" y="115" width="194" height="90" rx="3"/>
    <path class="van-seam" d="M232,128 L232,355 M390,112 L390,355 M415,112 L415,355"/>
    <rect class="rocker-stripe" x="280" y="340" width="310" height="22"/>
    <path class="rear-panel" d="M680,108 L862,108 Q882,112 882,140 L882,340 Q878,360 860,362 L620,362 Q650,240 680,108 Z"/>
    <path class="frond-graphic" role="img" aria-label="Stylised fern frond and spine graphic sweeping down the side" d="M618,108 L680,108 Q650,240 620,362 L574,362 Q614,280 618,108 Z"/>

    <rect class="brand-mark" x="702" y="146" width="12" height="12"/>
    <text class="brand-name" x="720" y="158">BRAMBLE COVE</text>
    <text class="brand-name" x="864" y="182" text-anchor="end" style="font-size:13px">THERAPY</text>

    <rect class="social-strip" x="805" y="240" width="26" height="92"/>
    <circle class="social-dot" cx="818" cy="256" r="6"/>
    <circle class="social-dot" cx="818" cy="277" r="6"/>
    <circle class="social-dot" cx="818" cy="298" r="6"/>
    <circle class="social-dot" cx="818" cy="319" r="6"/>

    <text class="phone-number" x="243" y="262">02937 418205</text>
    <text class="web-address" x="243" y="281">www.bramblecovecare.co.uk</text>
    <text class="email-address" x="402" y="296" text-anchor="end">info@bramblecovecare.co.uk</text>
    <text class="service-list" x="420" y="270" textLength="176" lengthAdjust="spacingAndGlyphs"><tspan class="service-bullet">•</tspan> Occupational Therapy <tspan class="service-bullet">•</tspan> Wheelchair Skills</text>
    <text class="service-list" x="440" y="281" textLength="140" lengthAdjust="spacingAndGlyphs"><tspan class="service-bullet">•</tspan> Private Wheelchair Assessment</text>

    <circle class="van-wheel" cx="215" cy="362" r="52"/><circle class="van-hub" cx="215" cy="362" r="20"/>
    <circle class="van-wheel" cx="735" cy="362" r="52"/><circle class="van-hub" cx="735" cy="362" r="20"/>
  </svg>

</main>
</body>
</html>
```